Need Stunning Website for Talent Acquisition (Recruiting) Agency

Hello, I am seeking a very professional, high-quality website that reflects our Talent Acquisition agency, Cobalt Kin. Our agency slogan is "Talent Acquisition. Differently." We are in fact different - we are a full service agency that provides services most others do not, and our website needs to immediately reflect that something is different about us when they visit our site.

This contest is to do complete website design and coding, including all graphics, features, plugins, and design elements. The graphics are very important on the site and must be of the highest professional quality. One critical aspect is that the imagery must convey that we serve clients in a variety of industries, including business, healthcare, churches and religious organizations, non-profits, manufacturing, retail, and more. We recruit for both professional level positions (e.g. CEO, COO, Pastor), as well as entry level (e.g. secretary, caregiver, factory worker).
The following pages should be designed:
Home Page - a captivating home page that immediately tells our brand story, what makes us different, and the value that we bring to the table.
Client Services Page - a page that talks more about the services we provide and why we produce better results. This page will cover the 5 C's in greater detail as well as all the things that make us different.
Industries - The industries we serve
Request Services - a page where clients can submit details about a job they would like us to recruit for, including attaching a job description if they have one
Candidates Page - a simple page that encourages prospective candidates to submit their resume for review
About Us - Common about us page
Blog - Common blog page
Contact Us - a contact page for general inquiries
The website must be built in an ultra-SEO friendly manner and optimized for speed and performance. As mentioned above, you will be responsible for providing all graphics for the site (copyright compliant).
The website will need to be compatible with Elementor Pro (I have subscription) and Yoast SEO. It needs to be designed on a high-quality wordpress theme that receives regular updates. It also needs instant chat messaging feature. Would like a traditional menu bar at the top of the page (not a fan of menu's that are hidden or put on the side of the page).

Please, please, please - - do NOT waste my time with generic/stock templates, low-quality graphics, etc. We are a PREMIUM agency and our website needs to reflect that.

In the future we will add a job board - I do not want that initially - but will want the option to add it later.

Must also have the ability to upload documents /attachments on the contact page/form.

It probably goes without saying, but the page must be fully responsive - suitable to work on all device types.

Target Market(s)

Businesses

Industry/Entity Type

Talent Acquisition (Recruiting) Agency

Coding

Coded - Design and coding required

Number of Pages Required

5+ page

Requirements
Must have
• Please see brief
Should not have
• No generic template/stock website or graphics - must have PREMIUM feel.

```html
<!DOCTYPE html>
<html lang="en">
<head>
<meta charset="UTF-8">
<title>Cobalt Kin — Talent Acquisition</title>
<link href="https://fonts.googleapis.com/css2?family=Poppins:wght@400;500;600&display=swap" rel="stylesheet">
<style>
  :root {
    --navy: #121c45;
    --page: #ffffff;
    --band: #f9f9f9;
    --footer: #f0f3fa;
    --muted: #5e6788;
    --line: #d6dae6;
    --box-line: #dde1ec;
    --accent: #f5b800;
    --accent-deep: #e29b00;
    --placeholder: #9aa1b9;
  }
  * { margin: 0; padding: 0; box-sizing: border-box; }
  html, body { width: 1200px; height: 905px; overflow: hidden; }
  body {
    position: relative;
    background: var(--page);
    font-family: "Poppins", sans-serif;
    color: var(--navy);
  }
  .top-band { position: absolute; left: 0; top: 0; width: 1200px; height: 76px; background: var(--band); }

  .cta-banner { position: absolute; left: 136px; top: 135px; width: 928px; height: 293px; background: var(--navy); }
  .cta-photo {
    position: absolute; left: 200px; top: 60px; width: 315px; height: 368px;
    background: linear-gradient(160deg, #6b4a32 0%, var(--accent) 38%, var(--accent-deep) 100%);
    border-radius: 140px 140px 0 0;
  }
  .cta-copy { position: absolute; left: 611px; top: 198px; color: #fff; }
  .cta-eyebrow { font-size: 13px; font-weight: 500; letter-spacing: 3.6px; text-transform: uppercase; }
  .cta-title { margin-top: 6px; font-size: 32.5px; font-weight: 600; line-height: 36px; width: 420px; }
  .cta-button {
    position: absolute; left: 611px; top: 339px; width: 133px; height: 38px;
    background: #fff; color: var(--navy); border-radius: 8px;
    font-size: 16px; font-weight: 500; display: flex; align-items: center; justify-content: center;
    text-decoration: none;
  }

  .site-footer { position: absolute; left: 0; top: 486px; width: 1200px; height: 419px; background: var(--footer); }
  .brand-name { position: absolute; left: 104px; top: 544px; font-size: 29px; font-weight: 600; color: var(--navy); letter-spacing: -0.5px; }
  .brand-text { position: absolute; left: 104px; top: 612px; width: 280px; font-size: 14px; line-height: 20px; color: var(--muted); }
  .social-list { position: absolute; left: 104px; top: 715px; display: flex; gap: 10px; list-style: none; }
  .social-list li {
    width: 41px; height: 41px; border: 1px solid var(--box-line); border-radius: 3px;
    display: flex; align-items: center; justify-content: center;
  }
  .social-list li span { width: 14px; height: 14px; background: var(--navy); border-radius: 2px; }

  .footer-col { position: absolute; top: 546px; }
  .footer-col h3 { font-size: 20.5px; font-weight: 600; line-height: 24px; color: var(--navy); }
  .footer-col ul { list-style: none; margin-top: 51px; }
  .footer-col li { font-size: 14px; line-height: 20px; height: 38.3px; color: var(--muted); }
  .col-features { left: 459px; }
  .col-links { left: 643px; }
  .col-news { left: 846px; }
  .news-text { margin-top: 51px; width: 240px; font-size: 14px; line-height: 20px; color: var(--muted); }
  .news-field {
    position: absolute; left: 846px; top: 679px; width: 251px; height: 40px;
    border: 1px solid var(--box-line); border-radius: 3px;
    display: flex; align-items: center; justify-content: space-between; padding: 0 16px;
    font-size: 12px; color: var(--placeholder);
  }

  .footer-rule { position: absolute; left: 0; top: 838px; width: 1200px; height: 1px; background: var(--line); }
  .copyright { position: absolute; left: 101px; top: 862px; font-size: 12.5px; color: var(--muted); }
  .legal-links { position: absolute; left: 921px; top: 862px; display: flex; align-items: center; font-size: 12.5px; color: var(--muted); }
  .legal-links .sep { width: 1px; height: 17px; background: var(--line); margin: 0 11px; }
</style>
</head>
<body>
  <div class="top-band"></div>

  <section class="cta-banner" aria-label="Call to action"></section>
  <div class="cta-photo" role="img" aria-label="Photo of a smiling woman in a yellow hoodie holding an open laptop"></div>
  <div class="cta-copy">
    <p class="cta-eyebrow">What are you waiting for?</p>
    <h2 class="cta-title">Find the talent to get your business growing</h2>
  </div>
  <a class="cta-button" href="#">Get Started</a>

  <footer class="site-footer"></footer>
  <div class="brand-name">Cobalt Kin</div>
  <p class="brand-text">Lorem ipsum dolor sit amet, consectetur adipiscing elit, sed do eiusmod tempor incididunt ut labore et dolore magna aliqua. Ut enim</p>
  <ul class="social-list" aria-label="Social profiles">
    <li><span></span></li><li><span></span></li><li><span></span></li><li><span></span></li>
  </ul>

  <div class="footer-col col-features">
    <h3>Features</h3>
    <ul><li>Help Desk</li><li>Knowledge Base</li><li>Embed Tools</li><li>Live Chat</li><li>Integrations</li></ul>
  </div>
  <div class="footer-col col-links">
    <h3>Quick Links</h3>
    <ul><li>Home</li><li>About</li><li>Features</li><li>Plans</li><li>Footer</li></ul>
  </div>
  <div class="footer-col col-news">
    <h3>Newsletter Personalized</h3>
    <p class="news-text">We’re a team of non-cynics who truly care for our work.</p>
  </div>
  <div class="news-field">
    <span>Type your email</span>
    <svg width="15" height="14" viewBox="0 0 15 14" aria-hidden="true">
      <path d="M14 1 L1 6 L6 8 L8 13 Z" fill="var(--placeholder)"/>
    </svg>
  </div>

  <div class="footer-rule"></div>
  <p class="copyright">Copyright © 2022 cobaltkin</p>
  <div class="legal-links"><span>Terms of Use</span><span class="sep"></span><span>Privacy Policy</span></div>
</body>
</html>
```